Domestic Building Company requires professional webpage

We have an existing webpage that was never completed. We are a growing building company specialising in domestic building, renovations and commercial maintenance. We liaise closely with each of our clients to provide quality service they would be happy to recommend. Our easy approachable staff give our clients the confidence to discuss their needs and changes they may have along the way.
Our main source of new customers have been from recommendations of existing clients.
We would like our webpage to reflect our eye for detail and showcase our previous work.
The colour theme should be the same as the colours of our logo.
We would like the main page to really stand out with a slideshow of our pictures of works we have completed.
We would like the tabs to remain the same - Home, About Us, Our Services, Contact us.
In the Our Services section we would like each sub heading to be a link where viewers can see pictures from previous work we have completed.
Our current web page is www.kestrelbuilding.com.au

```html
<!DOCTYPE html>
<html lang="en">
<head>
<meta charset="utf-8">
<title>Brightwall Building Services</title>
<link rel="stylesheet" href="https://fonts.googleapis.com/css2?family=Open+Sans:ital,wght@0,400;0,600;0,700;1,400;1,600&family=Roboto:wght@400;500;700&display=swap">
<style>
:root{
  --topbar:#0d5fb0;
  --link-green:#7fd13b;
  --page-bg:#e6e6e6;
  --panel:#ffffff;
  --ink:#1d1d1d;
  --muted:#6b6b6b;
  --nav:#444;
  --svc-yellow:#f8c431;
  --svc-red:#a33a40;
  --svc-navy:#124c7a;
  --svc-blue:#4a6ea8;
  --svc-green:#25a24f;
  --blog-bg:#fbe9a6;
  --blog-border:#e9d47c;
  --caption-bg:rgba(25,25,25,.72);
  --orange:#f07f1b;
  --band:#f2f2f2;
  --footer:#3d4048;
  --footer-text:#e4e5e8;
  --footer-muted:#9a9da4;
  --brand-green:#8cc63f;
}
*{box-sizing:border-box;margin:0;padding:0}
html,body{width:908px;height:1200px;overflow:hidden}
body{background:var(--page-bg);font-family:"Roboto",Arial,sans-serif;color:var(--ink)}
.canvas{position:relative;width:900px;height:1190px;transform:scale(1.0089);transform-origin:0 0;
  background:repeating-linear-gradient(45deg,#e9e9e9 0 2px,#e3e3e3 2px 4px)}
.abs{position:absolute}
a{color:inherit;text-decoration:none}

/* top bar */
.topbar{left:0;top:0;width:900px;height:19px;background:var(--topbar);color:#fff;font-size:10px}
.topbar .ask{left:142px;top:4px;font-weight:500;letter-spacing:.2px}
.topbar .contact{left:398px;top:4px;font-size:9px;white-space:nowrap}
.topbar .contact em{color:var(--link-green);font-style:italic}
.topbar .contact .phone{color:var(--link-green)}
.topbar .lang{left:686px;top:0;height:19px;width:48px;border-left:1px solid rgba(255,255,255,.2);border-right:1px solid rgba(255,255,255,.2);font-size:7px;padding:5px 0 0 17px}
.topbar .lang i{position:absolute;left:5px;top:6px;width:9px;height:6px;background:#c9d4ec}

/* header */
.header{left:0;top:19px;width:900px;height:58px;background:#fff;border-bottom:1px solid #d9d9d9}
.brand{left:137px;top:19px;display:flex;align-items:center;gap:6px}
.brand-mark{width:14px;height:14px;background:var(--svc-navy)}
.brand-name{font-family:"Roboto",sans-serif;font-size:15px;font-weight:500;color:var(--svc-navy);line-height:1}
.nav{top:37px;font-size:9.5px;color:var(--nav)}

/* main panel */
.panel{left:134px;top:77px;width:628px;height:818px;background:var(--panel)}
.hero{left:141px;top:79px;width:614px;height:228px;background:linear-gradient(180deg,#5b6a4e 0%,#7a5a3e 45%,#5c4634 70%,#6e8c48 100%)}
.hero-caption{left:491px;top:173px;width:264px;height:110px;background:var(--caption-bg);color:#fff;padding:7px 10px 0 15px;font-family:"Roboto",sans-serif}
.hero-caption h2{font-weight:400;font-size:12.5px;letter-spacing:.9px}
.hero-caption p{margin-top:16px;font-size:12.5px;line-height:16px;letter-spacing:.3px}

.services{left:151px;top:334px;width:148px}
.service{display:block;height:22px;margin-bottom:7.5px;color:#fff;font-size:12.5px;letter-spacing:.5px;padding:3px 0 0 19px;
  clip-path:polygon(0 0,100% 0,100% 100%,0 100%,6px 50%)}
.service.yellow{background:var(--svc-yellow)}
.service.red{background:var(--svc-red)}
.service.navy{background:var(--svc-navy);margin-top:1px}
.service.blue{background:var(--svc-blue);margin-top:1px}
.service.green{background:var(--svc-green)}
.feature-title{left:151px;top:485px;font-size:13px;font-weight:400;letter-spacing:.3px}
.feature-photo{left:150px;top:506px;width:148px;height:124px;background:linear-gradient(180deg,#6f7d5c 0%,#8a6b4a 45%,#6c9a40 100%)}

.welcome{left:323px;top:336px;width:232px}
.welcome h1{font-size:13.5px;font-weight:500;letter-spacing:.6px}
.welcome h3{font-size:13px;font-weight:400;color:var(--muted);margin-top:8px;letter-spacing:.5px}
.welcome p{margin-top:6px;font-size:7.4px;line-height:11.6px;color:#333;font-family:Arial,sans-serif}
.map{left:322px;top:485px;width:247px;height:145px;background:linear-gradient(135deg,#dfe6cf 0%,#cfdcb7 40%,#e5e0cf 70%,#d6dfc4 100%)}
.map-overlay{left:393px;top:520px;width:175px;height:80px;background:rgba(40,40,40,.78);color:#fff;font-family:"Open Sans",sans-serif;font-weight:700;text-align:right;padding:11px 6px 0 0}
.map-overlay .l1{font-size:15px;letter-spacing:1px}
.map-overlay .l2{font-size:14px;margin-top:6px;letter-spacing:.6px}

.blog{left:594px;top:336px;width:151px;height:315px;background:var(--blog-bg);border:1px solid var(--blog-border)}
.blog h2{position:absolute;left:9px;top:9px;font-size:13.5px;font-weight:500;color:#444}
.post{position:absolute;left:6px;width:139px}
.post-photo{width:139px;height:47px;background:linear-gradient(180deg,#6b7d8a,#7a5f48 60%,#565a48);position:relative}
.post-photo span{position:absolute;left:11px;bottom:2px;color:#fff;font-size:10px;letter-spacing:.5px}
.post p{margin-top:5px;padding:0 3px;font-size:7.2px;line-height:11.3px;color:#333;font-family:Arial,sans-serif}
.post .more{display:block;text-align:right;font-size:7.2px;text-decoration:underline;padding-right:4px;color:#333;font-family:Arial,sans-serif}

.projects-head{left:152px;top:673px;width:595px;height:16px}
.projects-head::before{content:"";position:absolute;left:0;right:0;top:8px;height:3px;background:#ececec}
.projects-head span{position:absolute;left:222px;top:0;padding:0 8px;background:#fff;font-size:13px;letter-spacing:.6px}
.proj{background:linear-gradient(180deg,#7e8a72 0%,#8b6b4c 40%,#6f9a45 100%)}
.proj.b{background:linear-gradient(180deg,#8fa0b3 0%,#8a5a48 35%,#9aa0a0 60%,#7e7a5a 100%)}
.proj-cap{font-size:7.4px;letter-spacing:.3px;color:#333;font-family:Arial,sans-serif}
.arrow{top:760px}

/* subscribe */
.subscribe{left:0;top:895px;width:900px;height:100px;background:var(--band)}
.subscribe h2{position:absolute;left:0;width:900px;top:20px;text-align:center;font-family:"Open Sans",sans-serif;font-style:italic;font-weight:400;font-size:16px;color:#555}
.subscribe h2 b{font-weight:600}
.subscribe .field{position:absolute;left:322px;top:49px;width:167px;height:27px;background:#fff;border:1px solid #d8d8d8;font-size:8px;color:#aaa;padding:8px 0 0 10px;font-family:"Open Sans",sans-serif}
.subscribe .btn{position:absolute;left:492px;top:49px;width:86px;height:27px;background:var(--orange);color:#fff;font-size:8.5px;font-weight:600;text-align:center;padding-top:8px;font-family:"Open Sans",sans-serif}

/* footer */
.footer{left:0;top:995px;width:900px;height:195px;background:var(--footer);color:var(--footer-text);font-family:"Open Sans",sans-serif}
.footer h4{position:absolute;top:16px;font-size:12px;font-weight:400}
.footer .lnk{position:absolute;font-size:8.5px;font-weight:600}
.footer .lnk::before{content:"›";margin-right:5px}
.f-brand{left:124px;top:74px;display:flex;align-items:center;gap:6px}
.f-brand .brand-name{color:#8f939b}
.f-brand .brand-mark{background:#6c7079}
.f-contact{position:absolute;left:520px;font-size:10px;display:flex;align-items:center;gap:6px}
.f-hours{left:520px;top:91px;font-size:8px;color:var(--footer-muted);font-weight:600}
.social{position:absolute;left:724px;font-size:8.5px;font-weight:600;display:flex;align-items:center;gap:7px}
.social i{display:inline-block;width:11px;height:11px;border-radius:50%}
.footer .rule{left:104px;top:141px;width:693px;height:1px;background:#52565f}
.footer .legal{top:163px;font-size:8.5px;color:#c9cbd0;font-weight:600}
</style>
</head>
<body>
<div class="canvas">

  <div class="abs topbar">
    <span class="abs ask">DO YOU NEED MORE INFORMATIONS ?</span>
    <span class="abs contact">email us: <em>hello@brightwall.com.au</em> &nbsp; or &nbsp;Call Us : <span class="phone">+61 (02) 4510 2278</span></span>
    <span class="abs lang"><i></i>ENG</span>
  </div>

  <header class="abs header">
    <div class="abs brand"><span class="brand-mark"></span><span class="brand-name">Brightwall Building Services</span></div>
    <a class="abs nav" style="left:446px">Home</a>
    <a class="abs nav" style="left:497px">Our Services</a>
    <a class="abs nav" style="left:580px">About Us</a>
    <a class="abs nav" style="left:646px">Blog</a>
    <a class="abs nav" style="left:697px">Contact Us</a>
  </header>

  <main class="abs panel"></main>

  <div class="abs hero" role="img" aria-label="Slideshow photo of a completed timber gazebo with shingle roof in a garden"></div>
  <div class="abs hero-caption">
    <h2>BRIEF DISCRIPTION OF WORK</h2>
    <p>Sample text goses here. Lore ipsum dolore sit amet. consectetur a dipisci ping elit.</p>
  </div>

  <nav class="abs services">
    <a class="service yellow">Service name</a>
    <a class="service red">Service name</a>
    <a class="service navy">Service name</a>
    <a class="service blue">Service name</a>
    <a class="service green">Service name</a>
  </nav>
  <h3 class="abs feature-title">Our Feature Project</h3>
  <div class="abs feature-photo" role="img" aria-label="Featured project photo of a timber gazebo on a lawn"></div>

  <section class="abs welcome">
    <h1>WELCOME NOTE GOES HERE</h1>
    <h3>Sample Text</h3>
    <p><b>Introduction text;</b> Lorem ipsum dolor sit amet, consectetur adipiscing elit. Sed eget mi ac nulla facilisis auctor. Integer elit dolor, euismod in posuere in, cursus quis nibh. Vestibulum bibendum cursus iaculis. Donec dapibus scelerisque pulvinar. Nulla pharetra sapien a mauris elementum sagittis. Pellentesque a tincidunt est, sed venenatis erat. Suspendisse at nulla neque. Fusce et nunc lacinia, varius metus vitae, blandit eros.</p>
  </section>
  <div class="abs map" role="img" aria-label="Map of the service area with location pins"></div>
  <div class="abs map-overlay"><div class="l1">DISCOVER US</div><div class="l2">by Map</div></div>

  <aside class="abs blog">
    <h2>Blog</h2>
    <article class="post" style="top:47px">
      <div class="post-photo" role="img" aria-label="Blog photo of a painted and netted project"><span>16 Feb 2014</span></div>
      <p>Lorem ipsum dolor sit amet, consectetur adipiscing elit. Sed eget mi ac nulla facilisis auctor. Integer elit dolor, euismod in posuere in.</p>
      <a class="more">Read more &gt;</a>
    </article>
    <article class="post" style="top:187px">
      <div class="post-photo" role="img" aria-label="Blog photo of a painted and netted project"><span>16 Feb 2014</span></div>
      <p>Lorem ipsum dolor sit amet, consectetur adipiscing elit. Sed eget mi ac nulla facilisis auctor. Integer elit dolor, euismod in posuere in.</p>
      <a class="more">Read more &gt;</a>
    </article>
  </aside>

  <div class="abs projects-head"><span>Our Finished Projects</span></div>
  <svg class="abs arrow" style="left:134px" width="10" height="26" viewBox="0 0 10 26"><path d="M8 1 2 13l6 12" fill="none" stroke="#555" stroke-width="1.2"/></svg>
  <svg class="abs arrow" style="left:742px" width="10" height="26" viewBox="0 0 10 26"><path d="M2 1l6 12-6 12" fill="none" stroke="#555" stroke-width="1.2"/></svg>
  <div class="abs proj" style="left:154px;top:707px;width:186px;height:124px" role="img" aria-label="Finished project: timber gazebo in a garden"></div>
  <div class="abs proj b" style="left:354px;top:710px;width:186px;height:124px" role="img" aria-label="Finished project: brick house with new fence and gate"></div>
  <div class="abs proj" style="left:551px;top:710px;width:186px;height:124px" role="img" aria-label="Finished project: timber gazebo in a garden"></div>
  <span class="abs proj-cap" style="left:154px;top:859px">LOREM IPSUM DOLOR SIT AMET</span>
  <span class="abs proj-cap" style="left:357px;top:859px">LOREM IPSUM DOLOR SIT AMET</span>
  <span class="abs proj-cap" style="left:555px;top:859px">LOREM IPSUM DOLOR SIT AMET</span>

  <section class="abs subscribe">
    <h2>Subscribe to Receive <b>Special Offers</b></h2>
    <div class="field">Enter Your Email Address</div>
    <div class="btn">SUBSCRIBE</div>
  </section>

  <footer class="abs footer">
    <div class="abs f-brand"><span class="brand-mark"></span><span class="brand-name">Brightwall</span></div>

    <h4 style="left:320px">Website Links</h4>
    <a class="lnk" style="left:320px;top:43px">Home</a>
    <a class="lnk" style="left:320px;top:66px">Search</a>
    <a class="lnk" style="left:320px;top:89px">Partners</a>
    <a class="lnk" style="left:320px;top:112px">About Us</a>
    <a class="lnk" style="left:413px;top:43px">Blog</a>
    <a class="lnk" style="left:413px;top:66px">Gallery</a>
    <a class="lnk" style="left:413px;top:89px">Imprint</a>
    <a class="lnk" style="left:413px;top:112px">Sitemap</a>

    <h4 style="left:520px">Contact Us</h4>
    <div class="f-contact" style="top:41px">
      <svg width="15" height="11" viewBox="0 0 15 11"><rect x=".5" y=".5" width="14" height="10" fill="none" stroke="#e4e5e8"/><path d="M.5.5l7 6 7-6" fill="none" stroke="#e4e5e8"/></svg>
      office@brightwall.com.au</div>
    <div class="f-contact" style="top:65px;font-size:8.5px;font-weight:600">
      <svg width="8" height="12" viewBox="0 0 8 12"><path d="M2 0h2l1 3-1.5 1c.5 1.6 1.3 2.7 2.3 3.6L7 7l1 2.5L6.5 12C3 11 0 6 1 1z" fill="#e4e5e8"/></svg>
      +61 (02) 4510 2279</div>
    <span class="abs f-hours">Mo to Fr from 09:00 - 17:00 CET</span>

    <h4 style="left:722px">Follow Us</h4>
    <a class="social" style="top:42px"><i style="background:#3b5998"></i>Social Page</a>
    <a class="social" style="top:65px"><i style="background:#2aa9e0"></i>Updates</a>
    <a class="social" style="top:88px"><i style="background:#0e76a8"></i>Network</a>
    <a class="social" style="top:111px"><i style="background:#dd4b39"></i>Community</a>

    <div class="abs rule"></div>
    <span class="abs legal" style="left:104px">Copyright © 2014</span>
    <span class="abs legal" style="left:239px">All Rights Reserved.</span>
    <span class="abs legal" style="left:726px;top:157px;font-weight:400">SiteMap</span>
  </footer>
</div>
</body>
</html>
```